A small electrical company designed a vehicle wrap for the Corvan Haulmark 360

We designed a vehicle wrap for a small Los Angeles electrical company specializing in electrical repairs, air conditioning repair and installation, electric vehicle charging station installation, and electrical upgrades. Our clientele primarily serves residential and commercial customers. To stay within our budget, we chose a clear, eye-catching electrical and air conditioning logo that combined fonts and graphics to create a memorable impression.
Target Market(s)
electrical repair & installation, cooling&heating ,EV charger installation
Industry/Entity Type
electrical and Air conditioning
Requirements
Must have
- phone number:(555)4820173 Lic#:2048736 website www.quorvelectric.example
Nice to have
- my vehicle is Corvan haulmark 360 high roof 148'WB cargo van

```html
<!DOCTYPE html>
<html lang="en">
<head>
<meta charset="utf-8">
<title>Quorv Electric Solution Inc – Vehicle Wrap</title>
<link href="https://fonts.googleapis.com/css2?family=Montserrat:wght@800&family=Oswald:wght@500&family=Roboto+Mono:wght@700&display=swap" rel="stylesheet">
<style>
  :root {
    --navy: #1f2c40;
    --orange: #ef9a2b;
    --white: #ffffff;
    --panel-edge: #d9dbde;
    --page: #ffffff;
  }
  html, body { margin: 0; padding: 0; overflow: hidden; background: var(--page); }
  .canvas { position: relative; width: 1200px; height: 1200px; overflow: hidden; }
  .wrap-panel {
    position: absolute; left: 120px; width: 960px; height: 300px;
    background: var(--white); border: 2px solid var(--panel-edge); border-radius: 18px; overflow: hidden;
  }
  .wrap-panel--a { top: 180px; }
  .wrap-panel--b { top: 620px; }
  .bands { position: absolute; inset: 0; }
  .brand-mark { position: absolute; background: var(--orange); }
  .brand-block { position: absolute; background: var(--navy); }
  .brand-name {
    position: absolute; margin: 0; font-family: "Montserrat", sans-serif; font-weight: 800;
    color: var(--navy); line-height: 1.05; letter-spacing: 0.5px;
  }
  .website {
    position: absolute; font-family: "Roboto Mono", monospace; font-weight: 700;
    color: var(--navy); letter-spacing: 1.5px;
  }
  .services {
    position: absolute; font-family: "Oswald", sans-serif; font-weight: 500;
    text-transform: uppercase; letter-spacing: 0.8px; white-space: nowrap;
  }
  .phone {
    position: absolute; font-family: "Montserrat", sans-serif; font-weight: 800; color: var(--navy);
    white-space: nowrap;
  }
  .licence { position: absolute; font-family: "Oswald", sans-serif; font-weight: 500; white-space: nowrap; }

  .wrap-panel--a .brand-mark { left: 50px; top: 34px; width: 84px; height: 84px; }
  .wrap-panel--a .brand-name { left: 156px; top: 34px; font-size: 38px; }
  .wrap-panel--a .website { left: 226px; top: 126px; font-size: 15px; }
  .wrap-panel--a .services { left: 60px; top: 163px; font-size: 14px; color: var(--white); }
  .wrap-panel--a .licence { left: 60px; top: 200px; font-size: 15px; color: var(--white); }
  .wrap-panel--a .phone { left: 760px; top: 178px; font-size: 21px; }

  .wrap-panel--b .brand-block { left: 0; top: 0; width: 200px; height: 225px; }
  .wrap-panel--b .brand-name { left: 228px; top: 40px; font-size: 36px; }
  .wrap-panel--b .website { left: 290px; top: 130px; font-size: 15px; }
  .wrap-panel--b .services { left: 250px; top: 181px; font-size: 10px; color: var(--navy); }
  .wrap-panel--b .phone { left: 760px; top: 176px; font-size: 21px; }
  .wrap-panel--b .licence { left: 768px; top: 206px; font-size: 11px; color: var(--orange); }
</style>
</head>
<body>
<main class="canvas">

  <section class="wrap-panel wrap-panel--a" aria-label="Wrap option one, driver side">
    <svg class="bands" viewBox="0 0 960 300" aria-hidden="true">
      <polygon points="0,158 690,158 712,190 0,190" fill="var(--orange)"/>
      <polygon points="0,190 712,190 770,300 0,300" fill="var(--navy)"/>
      <polygon points="726,190 746,190 804,300 784,300" fill="var(--orange)"/>
    </svg>
    <span class="brand-mark"></span>
    <h1 class="brand-name">QUORV ELECTRIC<br>SOLUTION INC</h1>
    <div class="website">WWW.QUORVELECTRIC.EXAMPLE</div>
    <div class="services">Electrical Repairs • Air Conditioning Repair and Installation</div>
    <div class="licence">Lic#: 2048736</div>
    <div class="phone">(555) 482-0173</div>
  </section>

  <section class="wrap-panel wrap-panel--b" aria-label="Wrap option two, driver side">
    <svg class="bands" viewBox="0 0 960 300" aria-hidden="true">
      <polygon points="200,178 690,178 705,198 200,198" fill="var(--orange)"/>
      <polygon points="0,225 200,225 200,198 705,198 760,300 0,300" fill="var(--navy)"/>
      <polygon points="718,198 736,198 790,300 772,300" fill="var(--orange)"/>
    </svg>
    <span class="brand-block"></span>
    <h2 class="brand-name">QUORV ELECTRIC<br>SOLUTION INC</h2>
    <div class="website">WWW.QUORVELECTRIC.EXAMPLE</div>
    <div class="services">Electrical • Cooling &amp; Heating • EV Charger Repair &amp; Installation</div>
    <div class="phone">(555) 482-0173</div>
    <div class="licence">Lic#: 2048736</div>
  </section>

</main>
</body>
</html>
```